Yard Sign Design Needed

Yard sign needed for mowing & landscaping company. Would like to use the top logo with black background which is attached. Would like MOWING to be in large standout letters. The word "landscaping" can be smaller and more artistic or omitted. Will need room for phone number once design is approved. The phone number will need to stand out and look identical/similar to the word 'MOWING"

```html
<!DOCTYPE html>
<html lang="en">
<head>
<meta charset="UTF-8">
<title>Mowing Landscaping Yard Sign</title>
<link rel="stylesheet" href="https://fonts.googleapis.com/css2?family=Audiowide&family=Orbitron:wght@600&display=swap">
<style>
  :root {
    --backdrop: #f1f1f1;
    --sign-white: #ffffff;
    --lawn-green: #86a80a;
    --ink-black: #111111;
    --grass-light: #9fd63a;
    --grass-deep: #4f9a12;
  }
  * { margin: 0; padding: 0; box-sizing: border-box; }
  html, body {
    width: 800px;
    height: 1200px;
    overflow: hidden;
    background: var(--backdrop);
  }
  .canvas {
    position: relative;
    width: 800px;
    height: 1200px;
  }
  .yard-sign {
    position: absolute;
    left: 40px;
    top: 330px;
    width: 720px;
    height: 540px;
    background: var(--sign-white);
    box-shadow: 0 4px 10px rgba(0, 0, 0, 0.25);
    overflow: hidden;
  }
  .sign-type {
    position: absolute;
    inset: 0;
    width: 720px;
    height: 540px;
  }
  .headline {
    font-family: "Audiowide", sans-serif;
    fill: var(--lawn-green);
  }
  .subline {
    font-family: "Orbitron", sans-serif;
    font-weight: 600;
    fill: var(--ink-black);
  }
  .company-name {
    font-family: "Orbitron", sans-serif;
    font-weight: 600;
    fill: var(--ink-black);
  }
  .company-mark { fill: var(--ink-black); }
  .phone-number {
    font-family: "Audiowide", sans-serif;
    fill: var(--lawn-green);
  }
  .grass-strip {
    position: absolute;
    left: 0;
    right: 0;
    bottom: 0;
    height: 100px;
    background: linear-gradient(to bottom, rgba(159, 214, 58, 0) 0%, rgba(159, 214, 58, 0.6) 25%, var(--grass-light) 45%, var(--grass-deep) 100%);
  }
</style>
</head>
<body>
  <main class="canvas">
    <section class="yard-sign">
      <div class="grass-strip" role="img" aria-label="Illustration of a row of fresh green grass blades along the bottom of the sign"></div>
      <svg class="sign-type" viewBox="0 0 720 540" xmlns="http://www.w3.org/2000/svg">
        <text class="headline" x="360" y="155" text-anchor="middle" font-size="124" textLength="613" lengthAdjust="spacingAndGlyphs">MOWING</text>
        <text class="subline" x="360" y="225" text-anchor="middle" font-size="50" textLength="464" lengthAdjust="spacingAndGlyphs">LANDSCAPING</text>
        <rect class="company-mark" x="279" y="312" width="38" height="38"/>
        <text class="company-name" x="327" y="330" font-size="20" textLength="110" lengthAdjust="spacingAndGlyphs">TORVALE</text>
        <text class="company-name" x="327" y="346" font-size="10" textLength="110" lengthAdjust="spacingAndGlyphs">CONTRACTORS LLC</text>
        <text class="phone-number" x="360" y="428" text-anchor="middle" font-size="60" textLength="512" lengthAdjust="spacingAndGlyphs">555-014-2368</text>
      </svg>
    </section>
  </main>
</body>
</html>
```